High end business card design for custom homebuilding company

Looking for a high end business card design that is unique and elegant. Can use embossing, foil printing, laser die cutting, or any high end printing technique or high end paper. Will upload current design so you can see the logo and what we are using currently, but we want something more unique and elegant. I included our logo to help with design.

Target Market(s)

High end custom home buyers of $1.5 million plus homes. Also real estate developers of high end communities.

Industry/Entity Type

Business

Contact Information for Business Card

Double sided. We want something very elegant and expensive looking. We are looking to incorporate a combination of perhaps linen paper or a high end paper, with foil stamping or embossing/debossing to make the card look unique, but still elegant. We tend to use blacks and golds, but are open to any ideas. Looking for creative and unique design.

Colors

Designer to choose colors to be used in the design.

Requirements
Must have
• High end, elegant look. Can use foil, embossing, or high end papers like linen. We want to make the card unique and interesting, but elegant and expensive looking.
Nice to have
• I am including just some cards I saw that looked interesting for one reason or another. I like a clean elegant design and like both the clean white style, and the blacks. So not sure if we want a black design or white. Would like to see both.

```html
<!DOCTYPE html>
<html lang="en">
<head>
<meta charset="utf-8">
<title>Ridgewell Custom Homes – Business Card</title>
<link rel="stylesheet" href="https://fonts.googleapis.com/css2?family=Cinzel:wght@400;600&family=Work+Sans:wght@400&display=swap">
<style>
  :root {
    --backdrop: #121212;
    --card: #262626;
    --card-edge: #2e2e2e;
    --foil-gold: #f6ee8a;
    --silver: #c9c9c9;
    --silver-dim: #8f8f8f;
    --ink-deep: #1a1a1a;
  }
  * { box-sizing: border-box; margin: 0; padding: 0; }
  html, body {
    width: 1200px; height: 900px; overflow: hidden;
    background: var(--backdrop);
  }
  .sheet {
    width: 1200px; height: 900px;
    display: flex; flex-direction: column; align-items: center; justify-content: center;
    gap: 36px;
  }
  .card {
    position: relative;
    width: 720px; height: 400px;
    background: linear-gradient(160deg, var(--card-edge), var(--card) 60%, #222);
    border-bottom: 6px solid var(--foil-gold);
    box-shadow: 0 12px 30px rgba(0,0,0,.6);
    overflow: hidden;
  }
  .brand {
    display: flex; align-items: center; gap: 14px;
    font-family: "Cinzel", serif; font-weight: 600; color: var(--silver);
  }
  .brand__dot {
    width: 22px; height: 22px; border-radius: 50%;
    background: var(--foil-gold);
  }
  .brand__name { font-size: 50px; letter-spacing: 1px; line-height: 1; }
  .brand__tagline {
    font-family: "Cinzel", serif; font-weight: 600; color: var(--silver);
    font-size: 14px; letter-spacing: 14px; margin-top: 6px; padding-left: 36px;
  }
  /* front */
  .card--front .brand-block {
    position: absolute; left: 120px; top: 120px;
  }
  .card--front .website {
    position: absolute; left: 0; right: 0; bottom: 48px; text-align: center;
    font-family: "Work Sans", sans-serif; font-size: 15px; letter-spacing: 4px;
    color: var(--silver-dim); text-transform: uppercase;
  }
  /* back */
  .card--back .brand-block {
    position: absolute; left: 48px; top: 150px;
  }
  .card--back .brand__name { font-size: 34px; }
  .card--back .brand__dot { width: 16px; height: 16px; }
  .card--back .brand__tagline { font-size: 10px; letter-spacing: 9px; padding-left: 30px; }
  .divider {
    position: absolute; left: 380px; top: 110px; width: 1px; height: 150px;
    background: var(--silver-dim);
  }
  .contact {
    position: absolute; left: 410px; top: 112px;
    color: var(--silver);
  }
  .contact__name {
    font-family: "Cinzel", serif; font-weight: 600; font-size: 26px; letter-spacing: 2px;
  }
  .contact__role {
    font-family: "Work Sans", sans-serif; font-size: 13px; letter-spacing: 2px;
    color: var(--silver-dim); margin: 4px 0 22px;
  }
  .contact__list { list-style: none; font-family: "Work Sans", sans-serif; font-size: 16px; letter-spacing: 1.5px; }
  .contact__list li { display: flex; align-items: center; gap: 12px; margin-bottom: 8px; }
  .contact__list svg { width: 14px; height: 14px; fill: none; stroke: var(--silver-dim); stroke-width: 1.6; }
</style>
</head>
<body>
<main class="sheet">
  <section class="card card--front">
    <div class="brand-block">
      <div class="brand"><span class="brand__dot"></span><span class="brand__name">RIDGEWELL</span></div>
      <div class="brand__tagline">CUSTOM HOMES</div>
    </div>
    <p class="website">www.ridgewellhomes.com</p>
  </section>

  <section class="card card--back">
    <div class="brand-block">
      <div class="brand"><span class="brand__dot"></span><span class="brand__name">RIDGEWELL</span></div>
      <div class="brand__tagline">CUSTOM HOMES</div>
    </div>
    <div class="divider"></div>
    <div class="contact">
      <h1 class="contact__name">Daniel Varga</h1>
      <p class="contact__role">DIRECTOR</p>
      <ul class="contact__list">
        <li><svg viewBox="0 0 16 16"><path d="M3 2l3 0 1 4-2 1c1 2 2 3 4 4l1-2 4 1 0 3c-6 1-12-5-11-11z"/></svg>+36 30 555 0142</li>
        <li><svg viewBox="0 0 16 16"><rect x="1.5" y="3.5" width="13" height="9"/><path d="M1.5 3.5l6.5 5 6.5-5"/></svg>info@ridgewellhomes.com</li>
        <li><svg viewBox="0 0 16 16"><circle cx="8" cy="8" r="6.5"/><path d="M1.5 8h13M8 1.5c-3 3.5-3 9.5 0 13M8 1.5c3 3.5 3 9.5 0 13"/></svg>www.ridgewellhomes.com</li>
      </ul>
    </div>
  </section>
</main>
</body>
</html>
```